Events Management Webpage

I am after a basic webpage for my events company Galorra based in Perth WA. It is a boutique events company that organises all kinds of events from corporate awards nights/gala balls, birthday celebrations, cocktail parties, quiz nights etc. I am wanting separate TABS for all of my services which are Corporate Events, Private Parties & Events, Venue Management, Wedding Planning, Event Design, My Desk Helper and of course a gallery and contact page. Galorra offers their services Australia wide if this can be made obvious on each of the pages.
The logo is quite pink - I do want Pink to be included on the page but I want the page to look sophisticated and designer not too girly and pink so that it appeals to all corporate markets mainly.
A small gallery or the ability to put in lots of pictures on each of the pages would be good as this is how people see my work.

Target Market(s)

Young event planners and Personal Assistants

Industry/Entity Type

Boutique

Requirements
Must have
• Separate TABS for each of my services.
A Contact Page
Nice to have
• Happy for designers to mess around with the logo and page colours.
Should not have
• I don't like the fonts to be too scripty and the colours too girly. I want the page to be stylish and modern and appeal to a high class market of corporate planners.

```html
<!DOCTYPE html>
<html lang="en">
<head>
<meta charset="utf-8">
<title>Galorra — Event &amp; Planning Services</title>
<link href="https://fonts.googleapis.com/css2?family=Arimo:wght@400;700&family=Roboto+Condensed:wght@700&display=swap" rel="stylesheet">
<style>
:root{
  --pink:#d1166a;
  --pink-dark:#b80f5a;
  --bar-grey:#6b6868;
  --text:#5b4a50;
  --title:#5a3346;
  --footer:#252525;
  --footer-low:#3b3b3b;
  --white:#ffffff;
}
*{margin:0;padding:0;box-sizing:border-box}
html,body{width:1200px;height:1062px;overflow:hidden;background:var(--white)}
body{position:relative;font-family:"Arimo",Arial,sans-serif;color:var(--text)}
.abs{position:absolute}

/* service tabs */
.service-tabs{left:0;top:0;width:1200px;height:31px;background:var(--bar-grey);border-bottom:1px dashed #bdbdbd}
.service-tabs a{font-family:"Roboto Condensed","Arial Narrow",sans-serif;font-weight:700;font-size:13px;color:#f2f2f2;text-decoration:none;line-height:31px;text-transform:uppercase;letter-spacing:.1px;position:absolute;top:0}

/* header */
.header-band{left:0;top:32px;width:1200px;height:82px;background:linear-gradient(#ffffff,#e4e4e4)}
.page-links{left:0;top:114px;width:1200px;height:31px;background:var(--pink)}
.page-links a,.page-links span{position:absolute;top:0;line-height:31px;color:var(--white);font-size:13px;text-decoration:none}
.brand-disc{left:464px;top:40px;width:286px;height:157px;border-radius:0 0 50% 50%/0 0 100% 100%;background:linear-gradient(#f6f6f6 40%,#d2d2d2);z-index:3;text-align:center}
.brand-mark{position:absolute;left:134px;top:10px;width:18px;height:18px;background:var(--pink)}
.brand-name{position:absolute;left:0;width:100%;top:56px;font-size:26px;font-weight:700;color:var(--pink);letter-spacing:.5px}
.brand-tag{position:absolute;left:0;width:100%;top:89px;font-size:16px;color:#555}

/* hero */
.hero{left:0;top:145px;width:1200px;height:393px;background:radial-gradient(ellipse at 45% 30%,#5a3aa8 0%,#2c1c40 35%,#120c10 70%,#070505 100%)}
.floor{left:0;top:538px;width:1200px;height:91px;background:linear-gradient(#7a4a2a,#5c371e)}
.floor-rim{left:0;top:629px;width:1200px;height:33px;background:#6d625e;border-top:1px solid #d8cfc9;border-bottom:1px dashed #cfcfcf}
.slider-arrow{top:491px;width:22px;height:38px}
.service-card{top:447px;width:200px;height:147px;background:var(--white);padding:5px;box-shadow:0 2px 6px rgba(0,0,0,.4)}
.service-card .photo{width:190px;height:108px}
.service-card .label{height:29px;background:linear-gradient(#e02a80,var(--pink-dark));color:var(--white);font-size:15px;line-height:29px;text-align:center}

/* content */
.section-icon{width:20px;height:20px;background:var(--pink)}
.section-title{font-size:21px;font-weight:700;color:var(--pink)}
.intro{left:172px;top:723px;width:569px;font-size:12px;line-height:20.4px;text-align:justify}
.intro p+p{margin-top:20.4px}
.event-list{left:767px;top:726px;width:281px}
.event-item{position:relative;height:71px;border-bottom:1px solid #d9d9d9}
.event-item:last-child{border-bottom:none}
.event-thumb{position:absolute;left:0;top:0;width:72px;height:55px;border:3px solid var(--white);box-shadow:0 0 3px rgba(0,0,0,.45);background:linear-gradient(135deg,#3a0a10,#b3121d 50%,#2a0608)}
.event-title{position:absolute;left:82px;top:0;font-size:15px;font-weight:700;color:var(--title)}
.event-text{position:absolute;left:82px;top:22px;width:192px;font-size:11px;line-height:15.5px}

/* footer */
.footer{left:0;top:958px;width:1200px;height:70px;background:var(--footer);border-top:2px dashed #cfcfcf}
.phone{left:165px;top:986px;height:20px;display:flex;align-items:center;gap:10px;color:var(--white);font-size:15px;font-weight:700}
.phone .gap{margin-left:14px}
.social{left:777px;top:979px;display:flex;gap:14px}
.social span{width:28px;height:28px;background:var(--white);border-radius:3px}
.legal{left:0;top:1028px;width:1200px;height:34px;background:var(--footer-low);color:var(--white);font-size:12px;line-height:34px;text-align:center;word-spacing:1px}
</style>
</head>
<body>

<nav class="service-tabs abs">
  <a href="#" style="left:161px">Corporate Events</a>
  <a href="#" style="left:312px">Private Parties &amp; Events</a>
  <a href="#" style="left:509px">Venue Management</a>
  <a href="#" style="left:673px">Wedding Planning</a>
  <a href="#" style="left:831px">Event Design</a>
  <a href="#" style="left:952px">My Desk Helper</a>
</nav>

<div class="header-band abs"></div>
<nav class="page-links abs">
  <a href="#" style="left:319px">Home</a><span style="left:370px">|</span><a href="#" style="left:388px">About us</a>
  <a href="#" style="left:766px">Gallery</a><span style="left:823px">|</span><a href="#" style="left:841px">Contact us</a>
</nav>

<div class="brand-disc abs">
  <span class="brand-mark"></span>
  <div class="brand-name">Galorra</div>
  <div class="brand-tag">Event &amp; Planning Services</div>
</div>

<div class="hero abs" role="img" aria-label="Banquet hall with violet stage lighting, round dining tables and palms"></div>
<div class="floor abs" role="img" aria-label="Polished timber floor"></div>
<div class="floor-rim abs"></div>

<svg class="slider-arrow abs" style="left:74px" viewBox="0 0 22 38"><polyline points="19,2 3,19 19,36" fill="none" stroke="#fff" stroke-width="3"/></svg>
<svg class="slider-arrow abs" style="left:1107px" viewBox="0 0 22 38"><polyline points="3,2 19,19 3,36" fill="none" stroke="#fff" stroke-width="3"/></svg>

<div class="service-card abs" style="left:166px">
  <div class="photo" role="img" aria-label="Boardroom with long table and wood panelling" style="background:linear-gradient(#c9a36a,#7a4a22)"></div>
  <div class="label">Corporate Events</div>
</div>
<div class="service-card abs" style="left:387px">
  <div class="photo" role="img" aria-label="Party stage with lit columns" style="background:linear-gradient(135deg,#1a1430,#5e3a9a 50%,#b01040)"></div>
  <div class="label">Private Parties &amp; Events</div>
</div>
<div class="service-card abs" style="left:607px">
  <div class="photo" role="img" aria-label="Large venue hall with blue lighting and guests" style="background:linear-gradient(#2a6a8a,#0e1e2a)"></div>
  <div class="label">Venue Management</div>
</div>
<div class="service-card abs" style="left:831px">
  <div class="photo" role="img" aria-label="Wedding reception with balloon arches" style="background:linear-gradient(#cfc6c0,#8a6d52)"></div>
  <div class="label">Wedding planing</div>
</div>

<span class="section-icon abs" style="left:178px;top:683px"></span>
<h1 class="section-title abs" style="left:214px;top:689px">Event Management at its finest</h1>
<div class="intro abs">
  <p>Lorem Ipsum is simply dummy text of the printing and typesetting industry. Lorem Ipsum has been the industry's standard dummy text ever since the 1500s, when an unknown printer took a galley of type and scrambled it to make a type specimen book. It has survived not only five centuries, but also the leap into electronic typesetting, remaining essentially unchanged. It was popularised in the 1960s with the release of Letterfix sheets containing Lorem Ipsum passages, and more recently with desktop publishing software like Pagecraft Studio including versions of Lorem Ipsum.</p>
  <p>Lorem Ipsum is simply dummy text of the printing and typesetting industry. Lorem Ipsum has been the industry's standard dummy text ever since the 1500s, when an unknown printer took a galley of type and scrambled it to make a type specimen book.</p>
</div>

<span class="section-icon abs" style="left:766px;top:681px;background:#c78a3a"></span>
<h2 class="section-title abs" style="left:801px;top:682px">Latest events</h2>
<div class="event-list abs">
  <div class="event-item">
    <div class="event-thumb" role="img" aria-label="Event hall with red lighting"></div>
    <div class="event-title">Lorem Ipsum is simply</div>
    <div class="event-text">Lorem Ipsum is simply dummy text of the printing and typesetting industry.</div>
  </div>
  <div class="event-item">
    <div class="event-thumb" role="img" aria-label="Event hall with red lighting"></div>
    <div class="event-title">Lorem Ipsum is simply</div>
    <div class="event-text">Lorem Ipsum is simply dummy text of the printing and typesetting industry.</div>
  </div>
  <div class="event-item">
    <div class="event-thumb" role="img" aria-label="Event hall with red lighting"></div>
    <div class="event-title">Lorem Ipsum is simply</div>
    <div class="event-text">Lorem Ipsum is simply dummy text of the printing and typesetting industry.</div>
  </div>
</div>

<footer>
  <div class="footer abs"></div>
  <div class="phone abs">
    <svg width="21" height="21" viewBox="0 0 21 21"><rect width="21" height="21" rx="3" fill="#fff"/><path d="M6 4 L9 4 L10 8 L8 9.5 Q9.5 12.5 11.5 13 L13 11 L17 12 L17 15 Q16 17 13.5 16.5 Q6 14 4.5 6.5 Q4.5 4.5 6 4Z" fill="#252525"/></svg>
    <span>Phone : +61 - 555019 (210)</span><span class="gap">+61 - 555019 (348)</span>
  </div>
  <div class="social abs" aria-label="Social links">
    <span></span><span></span><span></span><span></span><span></span>
  </div>
  <div class="legal abs">Copyright © 2012 Galorra event planing and services. &nbsp;&nbsp; Use of this website constitutes acceptance of our User Agreement</div>
</footer>

</body>
</html>
```